Mail - Scan, Sort & Forward - Web Design

We need a web design for a mail scan, store, view and forward service. It is a lifestyle service predicated on freedom, convenience, ease of access, ease of use, security, safety. It involves personal information and is accessed remotely.
No branding or style guide is yet complete so an open pallet is available but design should convey simplicity as it targets demographic 45-75 years travellers but also high net worth multi location professionals, miners and other multi-location workers.
Competitor sites are: (for business description examples)
www.quellarbox.example
www.trimbeldesk.example.au
www.norvandelsupply.example.au
Updates

Attached files are wireframes which show how the service will work (UI). You should use these to form ideas about your web design for the service. They are not templates nor am I looking for a UI dev (yet).

Target Market(s)

Travellers ( especially retirees) and multi-location workers eg miners

Industry/Entity Type

Business

Requirements
Must have
• Being a lifestyle site, the pages must be low on text, lite layout, imagery addressing the target market.
Navigation should be simple to use
Concept of visitor / member / client should be addressed. The user needs to be able to permission other user groups (read-only)
Talk to reasons why prospects want to use this service.
Nice to have
• access to view nearest Kelm Rout office.
Regular call to action like survey, quiz or did you know info which may keep the user returning to the site.
Campaign section which enables customising of campaigns on an ongoing basis
Ability to access and download Terms & conditions, brochures .pdf or other information.
Simulate how service works..video or webcast
Should not have
• Do not want heavy or dense text everywhere. Use imagery where possible. Icons should be thematic not isolated.

```html
<!DOCTYPE html>
<html lang="en">
<head>
<meta charset="utf-8">
<title>Online Mail Service</title>
<link rel="stylesheet" href="https://fonts.googleapis.com/css2?family=Arimo:wght@400;700&family=Open+Sans:wght@400;600;700;800&display=swap">
<style>
:root{
  --ink:#555557;
  --text:#4a4a4a;
  --muted:#777;
  --rule:#cfcfcf;
  --band:#eeedee;
  --sky:#45bdea;
  --sky-light:#7fd6f4;
  --sky-deep:#2aa9de;
  --pale:#e4f3fa;
  --white:#fff;
  --silver-top:#f4f4f4;
  --silver-bot:#cfcfcf;
  --dark:#232323;
}
*{margin:0;padding:0;box-sizing:border-box}
html,body{width:794px;height:1200px;overflow:hidden;background:var(--white)}
body{position:relative;font-family:"Open Sans",sans-serif;color:var(--text)}
.abs{position:absolute}
.page-frame{left:16px;top:16px;width:765px;height:1166px;border:1px solid var(--rule)}
.flag{left:438px;top:35px;width:19px;height:13px;background:var(--sky-deep);border:1px solid #999}
.lang-select{left:474px;top:32px;width:125px;height:19px;border:1px solid #c9c9c9;border-radius:2px;font:8px "Arimo",sans-serif;color:#777;padding:4px 7px;background:linear-gradient(#fff,#f0f0f0)}
.lang-select span{position:absolute;right:0;top:0;width:17px;height:17px;border-left:1px solid #ccc;text-align:center;font-size:8px;line-height:17px}
.top-btn{top:32px;height:17px;border:1px solid #a9d5e6;border-radius:2px;background:linear-gradient(#f4fbfe,var(--pale));font:700 8px "Arimo",sans-serif;color:#2b6f8c;text-align:center;line-height:15px}
.brand-name{left:109px;top:76px;font:700 37px "Arimo",sans-serif;color:var(--ink);letter-spacing:-.5px}
.brand-tag{left:111px;top:118px;font:11px "Arimo",sans-serif;color:#6a6a6a}
.main-nav{left:345px;top:94px;height:25px;display:flex;gap:5px}
.main-nav a{display:block;height:25px;background:linear-gradient(var(--sky-light),var(--sky));color:var(--white);font:700 10.5px "Arimo",sans-serif;text-decoration:none;text-align:center;line-height:25px}
.nav-rule{left:332px;top:124px;width:449px;height:1px;background:#eee}
.hero-photo{left:112px;top:168px;width:252px;height:241px;background:linear-gradient(#f2f2f2,#c9c9c9)}
.hero-title{left:410px;top:200px;font:600 30px "Open Sans",sans-serif;color:var(--ink);letter-spacing:-.3px}
.hero-sub{left:410px;top:233px;font:16px "Open Sans",sans-serif;color:var(--ink)}
.hero-copy{left:410px;top:271px;width:320px;font-size:9.6px;line-height:18.6px;color:var(--text)}
.btn-blue{height:22px;border-radius:2px;background:linear-gradient(var(--sky-light),var(--sky));color:var(--white);font:700 8.5px "Arimo",sans-serif;text-align:center;line-height:22px;box-shadow:0 1px 1px rgba(0,0,0,.2)}
.feature-band{left:16px;top:409px;width:765px;height:61px;background:var(--band);border-top:1px solid #dcdcdc;border-bottom:1px solid #dcdcdc}
.feature{top:429px}
.feature h4{font:600 9.5px "Open Sans",sans-serif;color:#2d2d2d}
.feature p{font-size:8px;color:var(--muted);margin-top:1px}
.section-title{font:400 15px "Open Sans",sans-serif;color:var(--ink);text-transform:uppercase}
.intro-copy{left:92px;top:550px;width:340px;font-size:8.8px;line-height:15.9px;color:var(--text)}
.video{left:488px;top:554px;width:227px;height:151px;background:var(--dark)}
.video-bar{left:488px;top:691px;width:227px;height:14px;background:linear-gradient(#e8e8e8,#bdbdbd)}
.finder{left:92px;top:747px;width:620px;height:74px;border:1px solid var(--rule)}
.finder-title{left:103px;top:764px;font:400 19px "Open Sans",sans-serif;color:var(--ink)}
.finder-sub{left:104px;top:790px;font-size:9.5px;color:var(--text)}
.btn-silver{border:1px solid #bbb;background:linear-gradient(var(--silver-top),var(--silver-bot));color:#a3a3a3;font:800 19px "Open Sans",sans-serif;text-align:center;text-shadow:0 1px 0 #fff;letter-spacing:-.5px}
.poll{left:92px;top:896px;width:169px;height:183px;border:1px solid #d7d7d7;border-radius:3px;box-shadow:0 2px 2px rgba(0,0,0,.1)}
.poll-q{left:112px;top:905px;width:130px;text-align:center;font:700 8.3px "Arimo",sans-serif;color:#333;line-height:13px}
.poll-sep{left:102px;top:937px;width:150px;height:1px;background:#e4e4e4}
.poll-opt{left:102px;width:151px;height:15px;border-radius:8px;background:#f1f1f1;font:8px "Arimo",sans-serif;color:#444;line-height:15px;padding-left:19px}
.poll-opt::before{content:"";position:absolute;left:7px;top:4px;width:7px;height:7px;border:1px solid #999;background:#fff}
.poll-link{left:153px;top:1047px;font:7.5px "Arimo",sans-serif;color:#888}
.poll-submit{left:206px;top:1040px;width:45px;height:21px;border:1px solid #bbb;border-radius:2px;background:linear-gradient(#f2f2f2,#d6d6d6);font:8.5px "Arimo",sans-serif;color:#999;text-align:center;line-height:19px}
.promo{left:308px;top:896px;width:405px;height:185px;background:linear-gradient(#7fd7f4,#4bc1ee)}
.promo-line{left:308px;width:405px;text-align:center;color:var(--white);font-family:"Open Sans",sans-serif;font-weight:800;letter-spacing:-.5px}
.social{top:1121px;width:20px;height:20px;border-radius:50%;background:#eef0f3;border:1px solid #d5d8dc}
.social i{position:absolute;left:5px;top:5px;width:8px;height:8px;border-radius:50%}
.footer-links,.footer-legal{top:1159px;font-size:8.2px;color:#555;word-spacing:1px}
.footer-links{left:91px}
.footer-legal{right:81px}
.sep{color:#999;margin:0 5px}
</style>
</head>
<body>
<div class="abs page-frame"></div>

<!-- utility bar -->
<div class="abs flag" role="img" aria-label="Language flag"></div>
<div class="abs lang-select">Choose Language...<span>&#8661;</span></div>
<div class="abs top-btn" style="left:620px;width:42px">Login</div>
<div class="abs top-btn" style="left:670px;width:43px">Sign Up</div>

<!-- brand -->
<div class="abs brand-name">Your Logo</div>
<div class="abs brand-tag">Keeping you intouch when your own the go!</div>

<!-- navigation -->
<nav class="abs main-nav">
  <a href="#" style="width:28px" aria-label="Home"><svg width="12" height="11" viewBox="0 0 12 11" style="margin-top:7px"><path d="M6 0 0 5.5h1.6V11h3.2V7.5h2.4V11h3.2V5.5H12z" fill="#fff"/></svg></a>
  <a href="#" style="width:68px">About Us</a>
  <a href="#" style="width:76px">How it works</a>
  <a href="#" style="width:69px">Pricing</a>
  <a href="#" style="width:35px">FAQs</a>
  <a href="#" style="width:69px">Contact Us</a>
</nav>
<div class="abs nav-rule"></div>

<!-- hero -->
<div class="abs hero-photo" role="img" aria-label="Photo of a smiling couple holding web and mail icon cards"></div>
<h1 class="abs hero-title">Online Mail Service</h1>
<div class="abs hero-sub">never get tied down by your mailbox again</div>
<p class="abs hero-copy">Get your mail and stay intouch, even if you travel or live overseas. Why wait? Get your important mail scanned and read it online within a day! So stay intouch when you plan on being away!</p>
<div class="abs btn-blue" style="left:410px;top:347px;width:98px">Find Out More</div>

<!-- feature band -->
<div class="abs feature-band"></div>
<div class="abs feature" style="left:97px"><h4>Ease of use</h4><p>Mail, scan, sort &amp; forward</p></div>
<div class="abs feature" style="left:232px"><h4>Ease of access</h4><p>Online mail access 24/7</p></div>
<div class="abs feature" style="left:360px"><h4>Freedom</h4><p>Live &amp; travel anywhere</p></div>
<div class="abs feature" style="left:483px"><h4>Piece of mind</h4><p>Protect your identity</p></div>
<div class="abs feature" style="left:603px"><h4>Security</h4><p style="margin-top:3px">Securely store your mail</p></div>

<!-- intro -->
<h2 class="abs section-title" style="left:92px;top:520px">Your Online Mail Service</h2>
<p class="abs intro-copy">A platform built to be simple convenient and reliable, with high security, 24/7 online mail access, you can have piece of mind you will be able to get your mail where ever and when ever!<br>Our online mail service couldn’t be easier! Get your documents scanned and read online with in a day, and be able to keep on top and manage your mail all by the click of a finger! View our video to find out more about our process!</p>
<div class="abs btn-blue" style="left:92px;top:672px;width:80px">Find Out More</div>

<!-- video -->
<h2 class="abs section-title" style="left:487px;top:520px">How It All Works</h2>
<div class="abs video"></div>
<svg class="abs" style="left:571px;top:594px" width="62" height="62" viewBox="0 0 62 62">
  <defs><radialGradient id="playFill" cx="50%" cy="35%" r="65%"><stop offset="0" stop-color="#8fe0ff"/><stop offset="1" stop-color="#1591d4"/></radialGradient></defs>
  <circle cx="31" cy="31" r="29" fill="url(#playFill)" stroke="#dff5ff" stroke-width="2"/>
  <path d="M24 18v26l21-13z" fill="#fff"/>
</svg>
<div class="abs video-bar"></div>
<svg class="abs" style="left:488px;top:691px" width="227" height="14" viewBox="0 0 227 14">
  <path d="M6 4v6l5-3z" fill="#444"/>
  <rect x="21" y="6" width="113" height="3" rx="1.5" fill="#777"/>
  <rect x="21" y="6" width="55" height="3" rx="1.5" fill="#e04a55"/>
  <circle cx="76" cy="7.5" r="3" fill="#eee" stroke="#888"/>
  <path d="M168 5h2l3-2v9l-3-2h-2z" fill="#444"/>
  <rect x="177" y="6" width="30" height="3" rx="1.5" fill="#555"/>
</svg>

<!-- post office finder -->
<div class="abs finder"></div>
<div class="abs finder-title">FIND YOUR NEAREST KELM ROUT OFFICE</div>
<div class="abs finder-sub">24/7 Access. Global Location. Security &amp; Privacy Protection. Easy Of Use.</div>
<div class="abs btn-silver" style="left:487px;top:762px;width:212px;height:43px;line-height:41px">FIND NEAREST NOW</div>

<!-- questionnaire -->
<h2 class="abs section-title" style="left:92px;top:862px">Questionnaire</h2>
<div class="abs poll"></div>
<div class="abs poll-q">Lorem ipsum dolor sit amet, consectetur adipisicing elit?</div>
<div class="abs poll-sep"></div>
<div class="abs poll-opt" style="top:951px">Definitely possible. I think.</div>
<div class="abs poll-opt" style="top:971px">Maybe, in the right conditions.</div>
<div class="abs poll-opt" style="top:990px">What you been smoking?</div>
<div class="abs poll-opt" style="top:1010px">I can swim faster than a shark.</div>
<div class="abs poll-link">view results</div>
<div class="abs poll-submit">Submit</div>

<!-- campaign -->
<h2 class="abs section-title" style="left:306px;top:862px">Advertisement</h2>
<div class="abs promo"></div>
<div class="abs promo-line" style="top:914px;font-size:22px">SIGN UP THIS MONTH AND GET</div>
<div class="abs promo-line" style="top:932px;font-size:61px;line-height:72px">HALF PRICE</div>
<div class="abs btn-silver" style="left:403px;top:1017px;width:211px;height:42px;line-height:40px">SIGN UP NOW!</div>

<!-- footer -->
<div class="abs social" style="left:91px"><i style="background:#3b5998"></i></div>
<div class="abs social" style="left:118px"><i style="background:#3fb4e6"></i></div>
<div class="abs social" style="left:145px"><i style="background:#f28a1d"></i></div>
<div class="abs footer-links">About Us<span class="sep">|</span>Tour<span class="sep">|</span>How It Works<span class="sep">|</span>Pricing<span class="sep">|</span>FAQs<span class="sep">|</span>Contact</div>
<div class="abs footer-legal">Terms &amp; Conditions<span class="sep">|</span>Privacy<span class="sep">|</span>© 2011 Your Logo</div>
</body>
</html>
```